Awesome law firm seeks great artwork for sign to be installed at local roller skating rink!!

We're a dynamic, law firm that does its work with a difference - we actually care about our clients and our fees are usually lower than most other firms.

We are installing a sign that's 78cm (height) x 158cm (width) to be printed on 3mm Aluminum Composite Panel and installed at a local roller skating rink in Kalamunda, Perth, Western Australia.

Graphics need to be provided in vector .eps (Encapsulated Post Script), .ai (Adobe Illustrator) or PDF format.

We have uploaded a copy of our Logo, which should feature on the sign (we usually have it on the top right of our stationery, but are happy to see other suggestions), together with our practice areas - Family Law, Wills and Estates, Building and Construction, Corporate and Commercial, Local Government, General legal (personal or business).

We don't have a 'slogan' for our firm, but for the roller skating rink sign, we're thinking of something like 'We roll with you", or something similar. Surprise us :)

Sign should also indicate that our team are local to "the Hills", which is how this area (the Kalamunda and surrounding areas of Perth) is known.

Main colors of the sign can include blue, white, black and red (more blue, white and black preferred).

The final design should communicate trust and expertise in law, but have a fun edge (the sign's at a roller skating rink after all and will be seen on every lap as it's in the rink).

The sign must include our website address www.pelbarnlegal.com (note this is still under construction in case you google us :)), our phone number 0491 607 238 and our main email address, which is admin@pelbarnlegal.com

Beyond this, we're happy to see any cool ideas for the design of our sign.

Target Market(s)

Local families and business owners at local roller skating rink

Industry/Entity Type

Legal services

Font styles to use
Serif
Other font styles liked:
• Designer to choose

Colors
0054AA
0677BA
7BADD7
CADEEF
E8F1F8
EB3D1F
EC4F4E
F09395
F8D3D4
FCEDEE

Requirements
Must have
• Logo, contact details, design as per description and can have the words "Get your skates on!"
Nice to have
• Awesome, striking, appealing design - easy to read as you're zooming past on your skates!
Should not have
• Any offensive, explicit, corny or suggestive words and preferably avoid cliché rhyming catch phrases, albeit we do want something fun that has a skating vibe

```html
<!DOCTYPE html>
<html lang="en">
<head>
<meta charset="utf-8">
<title>Pelbarn Legal – Rink Sign</title>
<link rel="stylesheet" href="https://fonts.googleapis.com/css2?family=Fira+Sans:wght@600&family=Noto+Serif:wght@400;700&display=swap">
<style>
  :root {
    --page: #ececed;
    --white: #ffffff;
    --rink-blue: #0080c4;
    --deep-blue: #00527f;
    --alert-red: #ea3036;
    --frame: #6d6e70;
    --peak-grey: #8a8b8e;
  }
  html, body {
    margin: 0;
    width: 1200px;
    height: 1200px;
    overflow: hidden;
    background: var(--page);
  }
  .canvas {
    position: relative;
    width: 1200px;
    height: 1200px;
  }
  .sign {
    position: absolute;
    left: 104px;
    top: 355px;
    width: 992px;
    height: 490px;
    display: block;
  }
  .headline-serif { font-family: "Noto Serif", Georgia, serif; font-weight: 700; }
  .firm-name { font-family: "Noto Serif", Georgia, serif; font-weight: 400; fill: var(--white); }
  .contact-line { font-family: "Fira Sans", Arial, sans-serif; font-weight: 600; fill: var(--white); font-size: 29px; }
</style>
</head>
<body>
<main class="canvas">
  <svg class="sign" viewBox="0 0 992 490" xmlns="http://www.w3.org/2000/svg" role="group" aria-label="Pelbarn Legal roller rink sign">
    <defs>
      <linearGradient id="panelBlue" x1="1" y1="0" x2="0" y2="1">
        <stop offset="0" stop-color="var(--deep-blue)"/>
        <stop offset="1" stop-color="var(--rink-blue)"/>
      </linearGradient>
      <linearGradient id="hillsTone" x1="0" y1="0" x2="1" y2="0">
        <stop offset="0" stop-color="#4a4a4d"/>
        <stop offset="0.45" stop-color="var(--rink-blue)"/>
        <stop offset="1" stop-color="var(--peak-grey)"/>
      </linearGradient>
    </defs>

    <rect class="sign-base" x="0.5" y="0.5" width="991" height="489" fill="var(--white)" stroke="var(--frame)" stroke-width="1"/>

    <path class="contact-panel" d="M741 0 C640 95 630 170 600 250 C570 340 530 390 444 490 L992 490 L992 0 Z" fill="url(#panelBlue)"/>

    <rect class="hills-illustration" x="0" y="20" width="620" height="137" fill="url(#hillsTone)" opacity="0.85" role="img" aria-label="Illustration of snow-capped hills in grey, black and blue"/>

    <path class="rink-band" d="M0 157 L645 157 L634 193 L0 193 Z" fill="var(--rink-blue)"/>

    <text class="headline-serif" x="67" y="278" font-size="80" fill="var(--alert-red)" textLength="325" lengthAdjust="spacingAndGlyphs">Get your</text>
    <text class="headline-serif" x="72" y="393" font-size="122" fill="var(--rink-blue)" textLength="450" lengthAdjust="spacingAndGlyphs">SKATES</text>
    <text class="headline-serif" x="440" y="449" font-size="76" fill="var(--alert-red)" stroke="var(--white)" stroke-width="4" paint-order="stroke">on</text>

    <g class="exclamation" fill="var(--alert-red)" stroke="var(--white)" stroke-width="4" paint-order="stroke">
      <path d="M547 298 Q547 281 564 281 Q581 281 581 298 L572 398 L556 398 Z"/>
      <circle cx="565" cy="430" r="21"/>
    </g>

    <text class="firm-name" x="961" y="213" font-size="50" text-anchor="end" letter-spacing="1">PELBARN</text>
    <text class="firm-name" x="961" y="311" font-size="80" text-anchor="end" letter-spacing="6">LEGAL</text>

    <text class="contact-line" x="961" y="383" text-anchor="end" letter-spacing="1">www.pelbarnlegal.com</text>
    <text class="contact-line" x="961" y="417" text-anchor="end" letter-spacing="1">admin@pelbarnlegal.com</text>
    <text class="contact-line" x="961" y="451" text-anchor="end" letter-spacing="1">0491 607 238</text>
  </svg>
</main>
</body>
</html>
```